Need Stunning Website for Talent Acquisition (Recruiting) Agency

Hello, I am seeking a very professional, high-quality website that reflects our Talent Acquisition agency, Cobalt Kin. Our agency slogan is "Talent Acquisition. Differently." We are in fact different - we are a full service agency that provides services most others do not, and our website needs to immediately reflect that something is different about us when they visit our site.

This contest is to do complete website design and coding, including all graphics, features, plugins, and design elements. The graphics are very important on the site and must be of the highest professional quality. One critical aspect is that the imagery must convey that we serve clients in a variety of industries, including business, healthcare, churches and religious organizations, non-profits, manufacturing, retail, and more. We recruit for both professional level positions (e.g. CEO, COO, Pastor), as well as entry level (e.g. secretary, caregiver, factory worker).
The following pages should be designed:
Home Page - a captivating home page that immediately tells our brand story, what makes us different, and the value that we bring to the table.
Client Services Page - a page that talks more about the services we provide and why we produce better results. This page will cover the 5 C's in greater detail as well as all the things that make us different.
Industries - The industries we serve
Request Services - a page where clients can submit details about a job they would like us to recruit for, including attaching a job description if they have one
Candidates Page - a simple page that encourages prospective candidates to submit their resume for review
About Us - Common about us page
Blog - Common blog page
Contact Us - a contact page for general inquiries
The website must be built in an ultra-SEO friendly manner and optimized for speed and performance. As mentioned above, you will be responsible for providing all graphics for the site (copyright compliant).
The website will need to be compatible with Elementor Pro (I have subscription) and Yoast SEO. It needs to be designed on a high-quality wordpress theme that receives regular updates. It also needs instant chat messaging feature. Would like a traditional menu bar at the top of the page (not a fan of menu's that are hidden or put on the side of the page).

Please, please, please - - do NOT waste my time with generic/stock templates, low-quality graphics, etc. We are a PREMIUM agency and our website needs to reflect that.

In the future we will add a job board - I do not want that initially - but will want the option to add it later.

Must also have the ability to upload documents /attachments on the contact page/form.

It probably goes without saying, but the page must be fully responsive - suitable to work on all device types.

Target Market(s)

Businesses

Industry/Entity Type

Talent Acquisition (Recruiting) Agency

Coding

Coded - Design and coding required

Number of Pages Required

5+ page

Requirements
Must have
• Please see brief
Should not have
• No generic template/stock website or graphics - must have PREMIUM feel.

```html
<!DOCTYPE html>
<html lang="en">
<head>
<meta charset="utf-8">
<title>Cobalt Kin — Talent Acquisition. Differently.</title>
<link href="https://fonts.googleapis.com/css2?family=Merriweather:ital,wght@0,700;0,900;1,900&family=Lato:wght@400;700&family=Montserrat:wght@400;500;600;700&display=swap" rel="stylesheet">
<style>
:root{
  --navy:#151b4f;
  --orange:#fbaa19;
  --orange-deep:#e8560f;
  --ink:#222;
  --muted:#555;
  --grey-bg:#eef0f4;
  --blog-bg:#f2f2f2;
  --footer:#050505;
  --rule:#8a6a14;
  --white:#fff;
}
*{margin:0;padding:0;box-sizing:border-box}
html,body{width:1200px;height:3812px;overflow:hidden}
body{position:relative;background:var(--white);font-family:'Lato',sans-serif;color:var(--ink)}
.abs{position:absolute}
.center{left:0;width:1200px;text-align:center}

/* header */
.site-header{top:0;left:0;width:1200px;height:85px;background:var(--white)}
.brand{left:98px;top:22px;font-family:'Montserrat',sans-serif;font-weight:700;font-size:36px;color:var(--navy);letter-spacing:-1px;line-height:40px}
.nav a{position:absolute;top:34px;font-family:'Montserrat',sans-serif;font-size:16px;color:#333;text-decoration:none;transform:translateX(-50%)}

/* hero */
.hero{top:85px;left:0;width:1200px;height:624px;background:linear-gradient(180deg,#d9dbdd 0%,#cfd1d4 60%,#c3c5c8 100%)}
.hero-people{left:130px;top:345px;width:940px;height:279px;background:linear-gradient(180deg,#c9c5c0 0%,#b9b2ab 40%,#3b4a6b 100%);border-radius:120px 120px 0 0;opacity:.85}
.hero-welcome{top:52px;font-family:'Montserrat',sans-serif;font-size:32px;color:var(--navy)}
.hero-title{top:98px;font-family:'Merriweather',serif;font-style:italic;font-weight:900;font-size:88px;color:var(--navy);line-height:110px}
.hero-slogan{top:216px;font-family:'Montserrat',sans-serif;font-size:26px;color:var(--white)}
.btn{display:inline-block;background:var(--orange);color:var(--white);font-family:'Montserrat',sans-serif;font-weight:600;border-radius:4px;text-align:center}
.hero-btn{left:520px;top:272px;width:159px;height:46px;line-height:46px;font-size:17px}
.hero-arrow{top:258px;width:24px;height:24px;border-radius:50%;background:var(--navy)}
.dots span{position:absolute;top:543px;width:13px;height:13px;border-radius:50%;background:var(--white)}

/* section heading */
.heading{font-family:'Merriweather',serif;font-weight:700;color:var(--navy);font-size:28px;line-height:40px;display:flex;justify-content:center;align-items:center;gap:20px}
.heading::before,.heading::after{content:"";width:74px;height:2px;background:var(--navy)}

/* positions */
.positions{top:709px;left:0;width:1200px;height:357px}
.pos{width:140px;text-align:center;transform:translateX(-50%)}
.pos .ring{width:118px;height:118px;border-radius:50%;background:var(--white);box-shadow:0 2px 10px rgba(0,0,0,.2);margin:0 auto;display:flex;align-items:center;justify-content:center}
.pos .ring.active{background:var(--orange);box-shadow:0 0 0 4px #fde2b0}
.pos .ring.outline{box-shadow:none;border:2px solid var(--orange)}
.pos .label{font-family:'Montserrat',sans-serif;font-size:26px;margin-top:22px;color:#111}

/* about */
.about{top:1066px;left:0;width:1200px;height:660px;background:linear-gradient(180deg,#e3e6ec 0%,#eef0f4 70%,#fff 100%)}
.about-text{top:1212px;left:120px;width:960px;text-align:center;font-size:17.5px;font-weight:400;line-height:33px;color:#333}
.about-btn{left:521px;top:1332px;width:158px;height:53px;line-height:53px;font-size:16px;box-shadow:0 3px 8px rgba(0,0,0,.15)}

/* industries */
.panel-navy{background:var(--navy);color:var(--white)}
.side-label{font-family:'Merriweather',serif;font-weight:900;font-size:25px;line-height:30px;writing-mode:vertical-rl;text-align:center;display:flex;align-items:center;justify-content:center}
.side-label.left{transform:rotate(180deg)}
.card-title{font-family:'Merriweather',serif;font-weight:900;font-size:25px}
.card-body{font-size:17px;line-height:32.5px;color:#e8e8f0}
.card-btn{width:160px;height:53px;line-height:53px;font-size:16px}
.carousel-arrow{width:38px;height:38px;background:var(--white);box-shadow:0 1px 4px rgba(0,0,0,.25);display:flex;align-items:center;justify-content:center}

/* video */
.video{left:108px;top:2082px;width:984px;height:462px;border:3px solid var(--orange-deep);border-radius:6px;background:linear-gradient(135deg,#6f6a64 0%,#a39a90 45%,#d9d4cc 70%,#7a6350 100%)}
.play{left:568px;top:2278px;width:64px;height:64px;border-radius:50%;background:#e31b1b;display:flex;align-items:center;justify-content:center;box-shadow:0 2px 8px rgba(0,0,0,.3)}

/* blog */
.blog{top:2630px;left:0;width:1200px;height:549px;background:var(--blog-bg)}
.post{top:2733px;width:309px;height:382px;background:var(--white);border-radius:8px;overflow:hidden;box-shadow:0 2px 10px rgba(0,0,0,.08);text-align:center}
.post .thumb{height:175px}
.post h3{font-family:'Merriweather',serif;font-weight:900;font-size:21px;color:#111;margin-top:24px}
.post p{font-family:'Montserrat',sans-serif;font-size:13px;line-height:26px;color:#444;margin:12px 18px 0}
.post a{display:inline-block;margin-top:12px;font-family:'Montserrat',sans-serif;font-size:16px;font-weight:500;color:#111;text-decoration:underline}
.post.featured{background:var(--navy)}
.post.featured h3,.post.featured p,.post.featured a{color:var(--white)}

/* footer */
.footer{top:3179px;left:0;width:1200px;height:633px;background:var(--footer);color:var(--white)}
.sub-title{top:3234px;font-family:'Montserrat',sans-serif;font-weight:700;font-size:28px}
.sub-text{top:3285px;font-size:16px}
.subscribe{left:228px;top:3330px;width:743px;height:55px;background:var(--white);border-radius:5px}
.subscribe span{position:absolute;left:20px;top:17px;font-family:'Montserrat',sans-serif;font-size:17px;color:#333}
.foot-h{font-family:'Montserrat',sans-serif;font-weight:600;font-size:19px}
.foot-links a{position:absolute;left:114px;font-family:'Montserrat',sans-serif;font-size:17px;color:var(--white);text-decoration:none}
.foot-brand{left:414px;top:3448px;width:380px;text-align:center;font-family:'Montserrat',sans-serif;font-weight:700;font-size:54px;letter-spacing:-1px;color:var(--orange);line-height:64px}
.foot-about{left:440px;top:3540px;width:320px;font-family:'Montserrat',sans-serif;font-size:14px;line-height:25.7px;text-align:justify}
.contact-line{font-family:'Montserrat',sans-serif;font-size:15px;display:flex;align-items:center;gap:12px}
.social span{position:absolute;top:3632px;width:38px;height:38px;border-radius:50%;border:2px solid var(--white)}
.foot-rule{left:111px;top:3722px;width:978px;height:1px;background:var(--rule)}
.copyright{top:3750px;font-family:'Montserrat',sans-serif;font-size:16px}
</style>
</head>
<body>

<header class="abs site-header">
  <div class="abs brand">Cobalt Kin</div>
  <nav class="nav">
    <a style="left:566px">HOME</a>
    <a style="left:681px">ABOUT</a>
    <a style="left:810px">SERVICES</a>
    <a style="left:932px">BLOG</a>
    <a style="left:1054px">CONTACT</a>
  </nav>
</header>

<section class="abs hero">
  <div class="abs hero-people" role="img" aria-label="Five professionals seated against a grey wall, reading documents and tablets"></div>
  <div class="abs center hero-welcome">WELCOME TO</div>
  <h1 class="abs center hero-title">Cobalt Kin</h1>
  <div class="abs center hero-slogan">"Talent Acquisition. Differently."</div>
  <span class="abs btn hero-btn">GET STARTED</span>
  <svg class="abs hero-arrow" style="left:53px" viewBox="0 0 24 24"><path d="M14 7l-5 5 5 5" stroke="#fff" stroke-width="2.5" fill="none"/></svg>
  <svg class="abs hero-arrow" style="left:1126px" viewBox="0 0 24 24"><path d="M10 7l5 5-5 5" stroke="#fff" stroke-width="2.5" fill="none"/></svg>
  <div class="dots">
    <span style="left:559px;background:var(--orange-deep);width:17px;height:17px;top:541px;border:2px solid #fff"></span>
    <span style="left:591px"></span>
    <span style="left:614px"></span>
    <span style="left:636px"></span>
  </div>
</section>

<section class="abs positions">
  <h2 class="abs center heading" style="top:45px">PROFESSIONAL-LEVEL POSITIONS</h2>
  <div class="abs pos" style="left:210px;top:145px">
    <div class="ring"><svg width="64" height="70" viewBox="0 0 64 70" fill="none" stroke="#222" stroke-width="2"><circle cx="32" cy="14" r="11"/><path d="M32 25v14M12 39h40M12 39v10M32 39v10M52 39v10"/><circle cx="12" cy="55" r="5"/><circle cx="32" cy="55" r="5"/><circle cx="52" cy="55" r="5"/></svg></div>
    <div class="label">CEO</div>
  </div>
  <div class="abs pos" style="left:476px;top:145px">
    <div class="ring active"><svg width="64" height="70" viewBox="0 0 64 70" fill="none" stroke="#fff" stroke-width="2.2"><path d="M16 34c-8 0-10-14 0-14 0-10 14-12 16-4 4-8 18-4 16 4 10 0 8 14 0 14z"/><path d="M18 34v10h28V34"/><path d="M12 56l40-8M14 62l38-10"/></svg></div>
    <div class="label">COO</div>
  </div>
  <div class="abs pos" style="left:743px;top:145px">
    <div class="ring outline"><svg width="64" height="70" viewBox="0 0 64 70" fill="none" stroke="#222" stroke-width="2"><rect x="20" y="6" width="24" height="24" rx="12"/><path d="M10 66V48c0-8 8-12 22-12s22 4 22 12v18"/><path d="M32 44v16M26 50h12"/></svg></div>
    <div class="label">Pastor</div>
  </div>
  <div class="abs pos" style="left:1008px;top:145px">
    <div class="ring"><svg width="64" height="70" viewBox="0 0 64 70" fill="none" stroke="#222" stroke-width="2"><rect x="30" y="10" width="18" height="18" rx="9"/><path d="M26 52V42c0-6 6-9 13-9s13 3 13 9v10"/><rect x="10" y="38" width="24" height="16"/><path d="M6 56h50"/></svg></div>
    <div class="label">secretary</div>
  </div>
</section>

<section class="abs about"></section>
<h2 class="abs center heading" style="top:1152px">ABOUT US</h2>
<p class="abs about-text">Lorem ipsum dolor sit amet, consectetur adipiscing elit, sed do eiusmod tempor incididunt ut labore et dolore magna aliqua. Ut enim ad minim veniam, quis nostrud exercitation ullamco laboris nisi ut aliquip ex ea commodo consequat. Duis aute irure dolor in reprehenderit in voluptate velit esse cillum dolore eu fugiat nulla pariatur.</p>
<span class="abs btn about-btn">LEARN MORE</span>

<h2 class="abs center heading" style="top:1445px;font-size:29px">OUR INDUSTRIES</h2>
<div class="abs panel-navy side-label left" style="left:99px;top:1560px;width:87px;height:325px">INCLUDING<br>BUSINESS</div>
<div class="abs" style="left:186px;top:1560px;width:151px;height:325px;background:linear-gradient(160deg,#d9c9b8,#b4523f 55%,#8fb0c8)" role="img" aria-label="Smiling businesswoman in a red jacket"></div>
<div class="abs" style="left:337px;top:1539px;width:277px;height:370px;background:linear-gradient(180deg,#e6e4e0 0%,#c9a58a 45%,#e3ad2a 80%,#f0ede6 100%)" role="img" aria-label="Young woman with glasses working at a laptop"></div>
<div class="abs panel-navy" style="left:614px;top:1512px;width:303px;height:416px">
  <div class="abs card-title" style="left:21px;top:28px">NON-PROFITS</div>
  <p class="abs card-body" style="left:25px;top:79px;width:232px">Lorem ipsum dolor sit amet, consectetur adipiscing elit, sed do eiusmod tempor incididunt ut labore et dolore magna aliqua. Ut enim ad minim veniam, quis nostrud exercitation</p>
  <span class="abs btn card-btn" style="left:33px;top:338px">LEARN MORE</span>
</div>
<div class="abs" style="left:917px;top:1560px;width:113px;height:325px;background:linear-gradient(180deg,#c8ced6,#5f86b6 55%,#e8ecef)" role="img" aria-label="Group of healthcare workers in scrubs and masks"></div>
<div class="abs panel-navy side-label" style="left:1030px;top:1560px;width:71px;height:325px">HEALTHCARE</div>
<div class="abs carousel-arrow" style="left:37px;top:1693px"><svg width="14" height="14" viewBox="0 0 14 14"><path d="M9 2L4 7l5 5" stroke="#111" stroke-width="2.5" fill="none"/></svg></div>
<div class="abs carousel-arrow" style="left:1132px;top:1693px"><svg width="14" height="14" viewBox="0 0 14 14"><path d="M5 2l5 5-5 5" stroke="#111" stroke-width="2.5" fill="none"/></svg></div>

<h2 class="abs center heading" style="top:2006px;font-size:26px">OUR VIDEO</h2>
<div class="abs video" role="img" aria-label="Colleagues walking through a bright open-plan office reviewing documents"></div>
<div class="abs play"><svg width="24" height="26" viewBox="0 0 24 26"><path d="M3 1l20 12L3 25z" fill="#fff"/></svg></div>
<div class="abs carousel-arrow" style="left:88px;top:2285px"><svg width="14" height="14" viewBox="0 0 14 14"><path d="M9 2L4 7l5 5" stroke="#111" stroke-width="2.5" fill="none"/></svg></div>
<div class="abs carousel-arrow" style="left:1073px;top:2285px"><svg width="14" height="14" viewBox="0 0 14 14"><path d="M5 2l5 5-5 5" stroke="#111" stroke-width="2.5" fill="none"/></svg></div>

<section class="abs blog"></section>
<h2 class="abs center heading" style="top:2663px">OUR BLOG</h2>
<article class="abs post" style="left:99px">
  <div class="thumb" role="img" aria-label="Diverse team laughing together in a meeting" style="background:linear-gradient(135deg,#5b4a3f,#c9a88a 50%,#3c4650)"></div>
  <h3>Sed ut perspiciatis</h3>
  <p>Lorem ipsum dolor sit amet, consectetur adipiscing elit, sed do eiusmod tempor incididunt ut labore et dolore magna</p>
  <a>Read More</a>
</article>
<article class="abs post featured" style="left:432px">
  <div class="thumb" role="img" aria-label="Business colleagues shaking hands in an office" style="background:linear-gradient(135deg,#3a3a3a,#d8d8d8 50%,#c96b3a)"></div>
  <h3>Sed ut perspiciatis</h3>
  <p>Lorem ipsum dolor sit amet, consectetur adipiscing elit, sed do eiusmod tempor incididunt ut labore et dolore magna</p>
  <a>Read More</a>
</article>
<article class="abs post" style="left:767px">
  <div class="thumb" role="img" aria-label="Smiling professionals gathered at a desk giving a thumbs up" style="background:linear-gradient(135deg,#e8e8e8,#8a7a6a 50%,#2f2f35)"></div>
  <h3>Sed ut perspiciatis</h3>
  <p>Lorem ipsum dolor sit amet, consectetur adipiscing elit, sed do eiusmod tempor incididunt ut labore et dolore magna</p>
  <a>Read More</a>
</article>

<footer class="abs footer"></footer>
<div class="abs center sub-title" style="color:#fff">Subscribe Today For New Updates</div>
<div class="abs center sub-text" style="color:#fff">Subscribe to our mailing list to get the updates to your email inbox....</div>
<div class="abs subscribe"><span>Enter your email</span>
  <svg class="abs" style="left:690px;top:15px" width="26" height="26" viewBox="0 0 24 24"><path d="M2 11L22 2l-7 20-3-8z" fill="#111"/><path d="M12 14l10-12" stroke="#fff" stroke-width="1.5"/></svg>
</div>

<div class="abs foot-h" style="left:112px;top:3438px;color:#fff">Quick Links</div>
<div class="foot-links">
  <a style="top:3494px">Home</a>
  <a style="top:3528px">About</a>
  <a style="top:3562px">Services</a>
  <a style="top:3596px">Blog</a>
  <a style="top:3630px">Contact</a>
</div>

<div class="abs foot-brand">Cobalt Kin</div>
<p class="abs foot-about" style="color:#fff">Lorem ipsum dolor sit amet, consectetur adipiscing elit, sed do eiusmod tempor incididunt ut labore et dolore magna aliqua. Ut enim ad minim veniam, quis nostrud exercitation ullamco laboris nisi ut aliquip ex ea commodo consequat. Duis aute irure dolor</p>

<div class="abs foot-h" style="left:907px;top:3451px;color:#fff">Get in touch</div>
<div class="abs contact-line" style="left:907px;top:3499px;color:#fff"><svg width="12" height="16" viewBox="0 0 12 16"><path d="M6 0a6 6 0 016 6c0 4-6 10-6 10S0 10 0 6a6 6 0 016-6z" fill="#fff"/><circle cx="6" cy="6" r="2" fill="#000"/></svg>Lorem ipsum dolor</div>
<div class="abs contact-line" style="left:907px;top:3542px;color:#fff"><svg width="16" height="12" viewBox="0 0 16 12" fill="none" stroke="#fff" stroke-width="1.5"><rect x="1" y="1" width="14" height="10"/><path d="M1 1l7 6 7-6"/></svg>info@cobaltkin.com</div>
<div class="abs foot-h" style="left:907px;top:3586px;color:#fff">Social Media</div>
<div class="social"><span style="left:909px"></span><span style="left:962px"></span><span style="left:1018px"></span></div>

<div class="abs foot-rule"></div>
<div class="abs center copyright" style="color:#fff">© copyrights 2022 2022 Cobalt Kin |&nbsp; All Rights Reserved</div>

</body>
</html>
```